KORVEL Flyer

We need a flyer for the research project called 'KORVEL'. We will distribute this flyer during conferences and events to our audience (mainly industry (Security and IoT), medical organisations, and researchers) in order to provide the basic information about the project.
The project will provide a Holistic Network Guard Framework for the Health-Care Industry.
We are attaching files to provide with concrete information on our requirements:
- KORVEL brochure content_final.ppt: includes the content we would like to include in the flyer. There is also the URL to the project website
- KORVEL layout.doc: it includes information about the layout (example video from another project brochure)
- KORVEL logo final version_sourcefile.zip: the project logo
- Logo-partners.zip: Logos that will be included (please follow the numbered order.)
We would like to use colors that belong to the project logo color range. Regarding the images that you may include in the brochure we wouldn't like to propose any because we do not want to limitate your imagination. They could be relevant to medical devices, security, etc.

```html
<!DOCTYPE html>
<html lang="en">
<head>
<meta charset="utf-8">
<title>KORVEL Flyer</title>
<link href="https://fonts.googleapis.com/css2?family=Montserrat:wght@400;500;600;700&family=Open+Sans:wght@400;600&display=swap" rel="stylesheet">
<style>
  :root{
    --teal:#1fa6a2;
    --teal-dark:#0d6e72;
    --teal-deep:#0a4f55;
    --teal-light:#bfe6e3;
    --ink:#3a4447;
    --muted:#7a8588;
    --paper:#ffffff;
    --line:#d7e3e3;
  }
  *{box-sizing:border-box;margin:0;padding:0}
  html,body{width:747px;height:1200px;overflow:hidden;background:var(--paper)}
  body{font-family:"Open Sans",Arial,sans-serif;color:var(--ink)}
  .flyer{width:747px;height:1200px;position:relative;background:var(--paper)}

  .masthead{height:84px;display:flex;align-items:center;justify-content:space-between;padding:0 36px}
  .brand{display:flex;align-items:center;gap:10px;font-family:"Montserrat",sans-serif;font-weight:700;font-size:26px;letter-spacing:3px;color:var(--teal)}
  .brand-dot{width:22px;height:22px;border-radius:50%;background:var(--teal)}
  .site-url{font-family:"Montserrat",sans-serif;font-size:11px;color:var(--teal-dark);letter-spacing:.5px}

  .hero{position:relative;height:470px;margin:0 36px;overflow:hidden}
  .hero-photo{position:absolute;inset:0;background:linear-gradient(160deg,#2fb8b2 0%,#15898a 45%,#0b5d63 100%)}
  .hero-label{position:absolute;font-family:"Montserrat",sans-serif;font-weight:600;color:#fff;font-size:19px;line-height:1.2}
  .hero-label.tl{left:28px;top:28px}
  .hero-label.tr{right:28px;top:28px;text-align:right}
  .hero-label.ml{left:28px;top:190px}
  .hero-label.mr{right:28px;top:190px;text-align:right}
  .hero-ring{position:absolute;left:50%;top:118px;width:150px;height:150px;margin-left:-75px;border:3px solid rgba(255,255,255,.85);border-radius:50%}
  .hero-title{position:absolute;left:0;right:0;top:300px;text-align:center;font-family:"Montserrat",sans-serif;font-weight:600;color:#fff;font-size:22px;line-height:1.25}

  .content{display:grid;grid-template-columns:1fr 1fr;gap:28px;padding:24px 36px 0;height:348px}
  .col h2{font-family:"Montserrat",sans-serif;font-size:12px;font-weight:700;color:var(--teal-dark);letter-spacing:1px;margin-bottom:8px}
  .col h3{font-family:"Montserrat",sans-serif;font-size:10px;font-weight:700;color:var(--teal);margin:8px 0 4px}
  .col p{font-size:9.5px;line-height:1.55;margin-bottom:6px}
  .col ul{list-style:none;font-size:9.5px;line-height:1.6;margin-bottom:6px}
  .col li::before{content:"";display:inline-block;width:5px;height:5px;background:var(--teal);margin-right:7px;vertical-align:middle}
  .contact{margin-top:10px;font-size:9px;color:var(--muted);line-height:1.6}
  .tagline{margin-top:14px;background:var(--teal);color:#fff;padding:16px 18px;font-family:"Montserrat",sans-serif;font-weight:600;font-size:15px;line-height:1.3}

  .partners{position:absolute;left:36px;right:36px;bottom:30px;border-top:2px solid var(--teal)}
  .partners h2{font-family:"Montserrat",sans-serif;font-weight:500;font-size:26px;color:var(--teal);text-align:center;margin:10px 0 14px}
  .partner-grid{display:grid;grid-template-columns:repeat(6,1fr);gap:12px 16px}
  .partner-badge{height:30px;border-radius:4px;background:var(--line)}
  .partner-badge.alt{background:var(--teal-light)}
  .partner-badge.dark{background:#c9d0d2}
</style>
</head>
<body>
<div class="flyer">
  <header class="masthead">
    <div class="brand"><span class="brand-dot"></span>KORVEL</div>
    <div class="site-url">www.korvel-project.eu</div>
  </header>

  <section class="hero">
    <div class="hero-photo" role="img" aria-label="Teal-toned photo of a hospital operating room with medical equipment"></div>
    <div class="hero-label tl">Medical and Health<br>Devices</div>
    <div class="hero-label tr">Healthcare<br>Services</div>
    <div class="hero-label ml">Cybersecurity</div>
    <div class="hero-label mr">Data Privacy</div>
    <div class="hero-ring"></div>
    <div class="hero-title">Cybersecurity<br>Vulnerability Assessment<br>and Certification</div>
  </section>

  <section class="content">
    <div class="col">
      <h2>WHAT IS KORVEL?</h2>
      <p>KORVEL is a three-year research project that builds tools to protect hospitals, clinics and connected medical devices against modern cyber threats.</p>
      <p>The framework brings together detection, assessment and response services in one open platform.</p>
      <h3>Key objectives</h3>
      <ul>
        <li>Assess risks of health devices</li>
        <li>Certify secure components</li>
        <li>Share threat intelligence</li>
        <li>Protect patient data</li>
      </ul>
      <div class="contact">Contact: info@korvel-project.eu<br>Follow us: @korvelproject</div>
    </div>
    <div class="col">
      <h2>WHY KORVEL?</h2>
      <p>Health-care systems hold sensitive records and run devices that must stay online. Attacks on them put patients at risk.</p>
      <ul>
        <li>Real-time anomaly detection</li>
        <li>Vulnerability assessment</li>
        <li>Privacy-preserving data sharing</li>
        <li>Certification services</li>
      </ul>
      <p>Results are validated in three pilot hospitals across Europe.</p>
      <div class="tagline">A Holistic Network Guard Framework for the Health Care Industry</div>
    </div>
  </section>

  <section class="partners">
    <h2>Partners</h2>
    <div class="partner-grid">
      <div class="partner-badge"></div><div class="partner-badge alt"></div><div class="partner-badge dark"></div>
      <div class="partner-badge"></div><div class="partner-badge alt"></div><div class="partner-badge dark"></div>
      <div class="partner-badge alt"></div><div class="partner-badge dark"></div><div class="partner-badge"></div>
      <div class="partner-badge alt"></div><div class="partner-badge"></div><div class="partner-badge dark"></div>
      <div class="partner-badge dark"></div><div class="partner-badge"></div><div class="partner-badge alt"></div>
      <div class="partner-badge dark"></div><div class="partner-badge alt"></div><div class="partner-badge"></div>
    </div>
  </section>
</div>
</body>
</html>
```